Wordpress Identity for Innovation Firm

Copper Lantern Partners is an innovation and investment firm based in Los Angeles.

We are seeking a designer that can help create our company identity and Wordpress site.

The attached Design Brief provides more details.

Designers Responsibility:

1) Company Identity

The designer will create the company identity.
Attached is a file that contains a type font that I like a lot.
No logo design is required.

The Copper Lantern Partners type font should become the company identity.
The attached document provides an overview of company type font identities that we like.

2) Wordpress Theme & Design

The designer will select existing Wordpress Themes that meet our design desires, and present them as part of the design proposal.

We will make our selection based on the selected Wordpress Theme(s), which the designer will creatively adapt with the new company identity.

Target Market(s)

We anticipate the website being mostly accessed by the US, Canada and European countries.

Our target audience includes the following:

• Corporations, companies, startups, non-profits
• Banks, venture capital, private equity, investors
• Incubators, accelerators, innovation clusters, research labs, universities
• Ad agencies, marketing agencies, digital agencies, media, press

Industry/Entity Type

Investment

Number of Pages Required

1 page

Font styles to use
Sans Serif
Other font styles liked:
• See attached design brief materials. The Font will represent the brand identity!

Requirements
Must have
• The ability to scroll through information top to bottom is important to us.
• This is in line with today's Wordpress themes.
• The website must be able to function across devices (desktop, tablet, phone).
• The top 5 web browsers and platforms (Mac/PC/Android/iOS)
• Contact us link or information field
Nice to have
• It would be nice to have a moving image in the background, such as:
• https://drifttrial.sitehatch.com
• The Wordpress theme of the moving image or video should be relevant to our overall Technology Innovation theme.
• Key words:
• Technology Innovation
• Digital
• Business
• Transportation
• Advanced Vehicles (auto, boat, airplane, rail, space)
• Space
• Venture Capital
• Investing
Should not have
• eCommerce

```html
<!DOCTYPE html>
<html lang="en">
<head>
<meta charset="utf-8">
<title>Copper Lantern Partners</title>
<link href="https://fonts.googleapis.com/css2?family=Open+Sans:ital,wght@0,300;0,400;0,600;0,700;1,400&display=swap" rel="stylesheet">
<style>
:root{
  --topbar:#1b1f2a;
  --nav:#1f66c9;
  --nav-active:#ffffff;
  --hero-dark:#2a2d33;
  --blue:#2f6fcf;
  --mission:#2c73d2;
  --skills-top:#1f5fa6;
  --skills-bottom:#6fa5d6;
  --ink:#222;
  --footer:#13243d;
  --footer-bottom:#0c1829;
  --footer-text:#b8c4d6;
  --white:#fff;
}
*{box-sizing:border-box;margin:0;padding:0}
html,body{width:682px;height:1200px;overflow:hidden;background:#fff}
body{font-family:"Open Sans",Arial,sans-serif;color:var(--ink);position:relative}
.topbar{height:26px;background:var(--topbar);display:flex;align-items:center;justify-content:space-between;padding:0 38px;color:#dfe4ec;font-size:10px}
.topbar .phone{display:flex;align-items:center;gap:6px}
.topbar .social{display:flex;gap:9px}
.topbar .social span{width:7px;height:7px;border-radius:50%;background:#dfe4ec;display:block}
.nav{height:24px;background:var(--nav);display:flex;justify-content:space-between;padding:0 42px}
.nav a{color:var(--white);font-size:9.5px;text-decoration:none;display:flex;align-items:center;padding:0 14px}
.nav a.active{background:var(--nav-active);color:var(--nav)}
.hero{position:relative;height:270px;background:linear-gradient(135deg,#3a3d44,#1e2025 55%,#4a4c52);overflow:hidden}
.hero h1{position:absolute;top:20px;left:70px;right:70px;color:var(--white);font-weight:600;font-size:17px;line-height:23px;text-align:center}
.video{position:absolute;left:155px;top:138px;width:375px;height:160px;background:#0f1a38;border:2px solid #fff}
.video .play{position:absolute;left:50%;top:50%;width:50px;height:50px;margin:-25px 0 0 -25px;border-radius:50%;background:#fff;display:flex;align-items:center;justify-content:center}
.mission{margin-top:100px;text-align:center;font-style:italic;color:var(--mission);font-size:12.5px}
.equation{display:flex;justify-content:center;align-items:flex-start;gap:22px;margin-top:22px}
.eq-item{width:110px;text-align:center;font-size:10px}
.eq-item .art{height:62px;width:70px;margin:0 auto 6px;border-radius:6px}
.eq-sign{font-size:46px;font-weight:300;line-height:62px;color:#111}
.skills{position:absolute;top:595px;left:0;width:682px;height:290px;background:linear-gradient(180deg,var(--skills-top),var(--skills-bottom) 70%,#3b6d9c)}
.skills h2{text-align:center;color:var(--white);font-weight:400;font-size:19px;margin-top:14px}
.skills .rule{width:140px;height:1px;background:#cfe0f2;margin:6px auto 0}
.skill-row{display:flex;justify-content:space-between;padding:0 45px;margin-top:34px}
.skill{width:137px;text-align:center;color:#0f1d33;font-size:10.5px;line-height:13px}
.skill .thumb{height:102px;border:3px solid #fff;margin-bottom:6px}
.partners{position:absolute;top:886px;left:0;width:682px}
.partners h2{text-align:center;font-weight:400;font-size:19px;color:#1c3f72;margin-top:6px}
.partners .rule{width:500px;height:1px;background:#9fb6d4;margin:4px auto 0}
.brand-row{display:flex;align-items:center;justify-content:space-between;padding:0 40px;margin-top:24px}
.brand-row .arrow{font-size:20px;color:#444}
.brand{font-size:14px;font-weight:700;color:#111;display:flex;align-items:center;gap:5px}
.brand .sq{width:12px;height:12px;background:#111}
.wave{position:absolute;top:990px;left:0}
.footer{position:absolute;top:1030px;left:0;width:682px;height:150px;background:var(--footer);display:flex;padding:18px 38px 0;gap:10px;color:var(--footer-text);font-size:7px;line-height:12px}
.footer h3{color:var(--white);font-size:8px;font-weight:700;margin-bottom:8px;letter-spacing:.3px}
.col{flex:1}
.col ul{list-style:none}
.col li::before{content:"› ";color:#7f93b0}
.signup{display:flex;margin-top:6px}
.signup span{background:#fff;color:#666;padding:0 6px;width:90px}
.signup b{background:var(--nav);color:#fff;padding:0 6px;font-weight:600}
.follow li::before{content:"";display:inline-block;width:7px;height:7px;border-radius:50%;background:#fff;margin-right:6px;vertical-align:middle}
.copyright{position:absolute;top:1180px;left:0;width:682px;height:20px;background:var(--footer-bottom);color:#8a98ad;font-size:7px;text-align:center;line-height:20px}
</style>
</head>
<body>
<header class="topbar">
  <div class="phone">
    <svg width="9" height="9" viewBox="0 0 24 24"><path fill="#dfe4ec" d="M6.6 10.8a15.1 15.1 0 0 0 6.6 6.6l2.2-2.2c.3-.3.7-.4 1-.2 1.1.4 2.3.6 3.6.6.6 0 1 .4 1 1V20c0 .6-.4 1-1 1A17 17 0 0 1 3 4c0-.6.4-1 1-1h3.5c.6 0 1 .4 1 1 0 1.3.2 2.5.6 3.6.1.3 0 .7-.2 1z"/></svg>
    +1 310-555-0142
  </div>
  <div class="social"><span></span><span></span><span></span></div>
</header>
<nav class="nav">
  <a class="active">Home</a><a>About Company</a><a>Our Services</a><a>Our Projects</a><a>Blog</a><a>Contact Us</a>
</nav>
<section class="hero" role="img" aria-label="Collage of magazine covers and brand pages in dark tones">
  <h1>Copper Lantern Partners is an innovation and investment firm, which creates sustainable competitive advantage through de-risked partnership model-sand superior operating performance.</h1>
  <div class="video"><div class="play"><svg width="20" height="22" viewBox="0 0 20 22"><path d="M3 1l16 10L3 21z" fill="#1f66c9"/></svg></div></div>
</section>
<p class="mission">Our mission as an innovation and investment firm is to help our clients to develop their business .</p>
<section class="equation">
  <div class="eq-item"><div class="art" role="img" aria-label="Illustration of a figure climbing a rising chart" style="background:linear-gradient(135deg,#e8eef6,#c9d6e6)"></div>Your Challenges</div>
  <div class="eq-sign">+</div>
  <div class="eq-item"><div class="art" role="img" aria-label="Illustration of two figures supporting each other" style="background:linear-gradient(135deg,#8fd3f0,#2a8fcf)"></div>Our Support</div>
  <div class="eq-sign">=</div>
  <div class="eq-item"><div class="art" role="img" aria-label="Thumbs up illustration" style="background:linear-gradient(135deg,#6fa8e6,#2a6fc4)"></div>Success</div>
</section>
<section class="skills" role="img" aria-label="Blue-toned city skyline backdrop">
  <h2>Our Awesome Skills</h2>
  <div class="rule"></div>
  <div class="skill-row">
    <div class="skill"><div class="thumb" role="img" aria-label="Business team meeting photo" style="background:linear-gradient(135deg,#c9d2da,#6e7c8a)"></div>We transform business challenges into significant growth opportunities</div>
    <div class="skill"><div class="thumb" role="img" aria-label="Business handshake photo" style="background:linear-gradient(135deg,#d6dde3,#5c6670)"></div>We partner with companies to develop new strategies</div>
    <div class="skill"><div class="thumb" role="img" aria-label="Colleagues collaborating at a desk photo" style="background:linear-gradient(135deg,#e2e6ea,#8a96a2)"></div>Collaboration</div>
    <div class="skill"><div class="thumb" role="img" aria-label="Wooden blocks spelling a result photo" style="background:linear-gradient(135deg,#d9c7a8,#7a6a52)"></div>Outcomes</div>
  </div>
</section>
<section class="partners">
  <h2>Our Brand Partners</h2>
  <div class="rule"></div>
  <div class="brand-row">
    <span class="arrow">‹</span>
    <span class="brand">Halvor</span>
    <span class="brand"><span class="sq"></span>Brenmoor</span>
    <span class="brand">Northbay Wear</span>
    <span class="brand">Orvane Group</span>
    <span class="brand"><span class="sq"></span>Pinecrest</span>
    <span class="brand">Fernlight</span>
    <span class="arrow">›</span>
  </div>
</section>
<svg class="wave" width="682" height="42" viewBox="0 0 682 42">
  <path d="M0 20 C200 44 420 0 682 16 L682 42 L0 42z" fill="#1f66c9"/>
  <path d="M0 30 C220 46 440 10 682 26 L682 42 L0 42z" fill="#13243d"/>
</svg>
<footer class="footer">
  <div class="col"><h3>QUICK LINKS</h3><ul><li>Home</li><li>About Company</li><li>Our Services</li><li>Our Projects</li><li>Blog</li><li>Contact Us</li></ul></div>
  <div class="col"><h3>CONTACT INFORMATION</h3><p>● 123 Orchard Lane, Suite 40, Los Angeles, CA</p><p>● +1 310-555-0142</p><p>● hello@copperlantern.com</p></div>
  <div class="col"><h3>NEWSLETTER SIGNUP</h3><p>Please enter your email address to receive our latest updates.</p><div class="signup"><span>Email address</span><b>Subscribe</b></div></div>
  <div class="col follow"><h3>FOLLOW US</h3><ul><li>Circlefeed</li><li>Birdline</li><li>Clipstream</li></ul></div>
</footer>
<div class="copyright">Copyright 2016 . All Rights Reserved</div>
</body>
</html>
```